Header image for law blog

I need a header image for my blog at www.prairiecourtledger.net.

The colors would match the current site. It would say: "Court Ledger: Estate Planning and Real Estate in the Land of Lincoln."

I also want to add in smaller type "Law Office of Ned Pyrkett 555 014 7283 ned@kettbar.com."

The theme maker suggests a header size of 1600 × 230 pixels.

```html
<!DOCTYPE html>
<html lang="en">
<head>
<meta charset="utf-8">
<title>Court Ledger</title>
<link rel="stylesheet" href="https://fonts.googleapis.com/css2?family=Bitter:ital,wght@0,400;0,700;1,400&family=Source+Sans+3:wght@400;600;700&display=swap">
<style>
  :root {
    --header-orange: #e05d22;
    --header-deep: #d6501a;
    --header-art: #eb7a40;
    --rule-white: #ffffff;
    --nav-cream: #f7f5e7;
    --widget-cream: #f7f5e7;
    --ink: #141412;
    --link-red: #bc360a;
    --title-orange: #ea9629;
    --field-border: #d4d0ba;
    --button-orange: #e05d22;
    --button-shadow: #b93207;
    --share-grey: #c9c9c9;
  }
  * { box-sizing: border-box; margin: 0; padding: 0; }
  html, body { width: 1200px; height: 761px; overflow: hidden; background: #fff; }
  body { position: relative; font-family: "Source Sans 3", "Helvetica Neue", Arial, sans-serif; color: var(--ink); }

  .site-header {
    position: absolute; left: 0; top: 0; width: 1200px; height: 170px;
    background: linear-gradient(180deg, var(--header-orange), var(--header-deep));
    overflow: hidden;
  }
  .header-scales { position: absolute; left: 40px; top: 14px; width: 120px; height: 136px;
    background: radial-gradient(ellipse at 50% 50%, var(--header-art) 0%, rgba(235,122,64,0.55) 70%, rgba(235,122,64,0) 100%); border-radius: 8px; }
  .header-skyline { position: absolute; left: 760px; top: 22px; width: 430px; height: 148px;
    background: linear-gradient(180deg, rgba(235,122,64,0) 0%, rgba(235,122,64,0.6) 45%, var(--header-art) 100%); }
  .site-title { position: absolute; left: 212px; top: 12px; font-family: "Bitter", Georgia, serif; font-weight: 700; font-size: 62px; line-height: 72px; color: #fff; letter-spacing: 0.5px; }
  .header-rule { position: absolute; left: 213px; width: 530px; height: 1.5px; background: var(--rule-white); }
  .site-tagline { position: absolute; left: 213px; top: 92px; font-size: 19px; line-height: 26px; color: #fff; letter-spacing: 0.3px; }
  .site-tagline strong { font-family: "Bitter", Georgia, serif; font-weight: 700; }
  .site-contact { position: absolute; left: 213px; top: 132px; display: flex; gap: 14px; font-size: 14.5px; color: #fff; }
  .site-contact span { display: flex; align-items: center; gap: 4px; }
  .site-contact svg { width: 13px; height: 13px; }

  .site-nav { position: absolute; left: 0; top: 170px; width: 1200px; height: 34px; background: var(--nav-cream); }
  .site-nav a { position: absolute; top: 10px; font-size: 11.5px; color: var(--ink); text-decoration: none; }
  .site-nav svg { position: absolute; left: 953px; top: 178px; }

  .entry { position: absolute; left: 252px; top: 232px; width: 450px; }
  .entry-title { font-family: "Bitter", Georgia, serif; font-weight: 400; font-size: 36.5px; line-height: 46px; color: var(--title-orange); text-decoration: underline; text-decoration-thickness: 2px; text-underline-offset: 5px; }
  .entry-meta { margin-top: 13px; display: flex; gap: 11px; font-size: 10px; color: var(--link-red); }
  .entry-meta span { display: flex; align-items: center; gap: 3px; }
  .entry-content { margin-top: 20px; font-size: 12.3px; line-height: 17.9px; }
  .entry-content p + p { margin-top: 17.9px; }
  .entry-content a { color: var(--link-red); text-decoration: none; }
  .share-heading { margin-top: 18px; font-weight: 700; font-size: 12px; }
  .share-row { display: flex; gap: 4px; margin-top: 4px; }
  .share-row i { display: block; width: 11px; height: 11px; background: var(--share-grey); border-radius: 2px; }
  .comment-link { margin-top: 15px; font-size: 10px; color: var(--link-red); display: flex; align-items: center; gap: 4px; }

  .widget { position: absolute; left: 755px; width: 221px; background: var(--widget-cream); padding: 15px 14px; }
  .widget-title { font-family: "Source Sans 3", sans-serif; font-style: italic; font-weight: 400; font-size: 15px; line-height: 20px; margin-bottom: 10px; }
  .widget a { display: block; color: var(--link-red); font-size: 10.5px; line-height: 23px; text-decoration: none; }
  .widget p, .widget label { font-size: 10px; line-height: 12.5px; display: block; }
  .widget input { display: block; width: 192px; height: 23px; border: 2px solid var(--field-border); background: #fff; margin: 8px 0 19px; }
  .subscribe { display: block; margin: 14px 0 0 20px; width: 153px; height: 30px; background: var(--button-orange); border: none; border-bottom: 3px solid var(--button-shadow); border-radius: 2px; color: #fff; font-family: inherit; font-weight: 700; font-size: 10.5px; }
</style>
</head>
<body>
  <header class="site-header">
    <div class="header-scales" role="img" aria-label="Scales of justice illustration"></div>
    <div class="header-skyline" role="img" aria-label="City skyline illustration with trees"></div>
    <h1 class="site-title">Court Ledger</h1>
    <div class="header-rule" style="top:86px"></div>
    <p class="site-tagline">Estate Planning and Real Estate in <strong>The Land of Lincoln</strong></p>
    <div class="header-rule" style="top:122px"></div>
    <div class="site-contact">
      <span><svg viewBox="0 0 12 12"><path d="M6 1 L11 6 H9.5 V11 H7 V8 H5 V11 H2.5 V6 H1 Z" fill="#f7c442"/></svg>Law Office of Ned Pyrkett</span>
      <span><svg viewBox="0 0 12 12"><path d="M2.5 1 L4.5 1 L5.5 3.8 L4.2 5 Q5.3 7 7 7.8 L8.2 6.5 L11 7.5 L11 9.5 Q10.5 11 8.5 11 Q2 10 1 3.5 Q1 1.5 2.5 1 Z" fill="#f7c442"/></svg>555 014 7283</span>
      <span><svg viewBox="0 0 12 12" fill="none" stroke="#f7c442" stroke-width="1.2"><circle cx="6" cy="6" r="5"/><ellipse cx="6" cy="6" rx="2.2" ry="5"/><path d="M1 6 H11"/></svg>ned@kettbar.com</span>
    </div>
  </header>

  <nav class="site-nav">
    <a href="#" style="left:207px">About us</a>
    <a href="#" style="left:278px">Archives</a>
  </nav>
  <svg style="position:absolute;left:953px;top:178px" width="18" height="18" viewBox="0 0 18 18" fill="none" stroke="#141412" stroke-width="2"><circle cx="7.5" cy="7.5" r="5.5"/><path d="M11.5 11.5 L16.5 16.5"/></svg>

  <article class="entry">
    <h2 class="entry-title">FHA 90-day seasoning requirement is back for flips</h2>
    <div class="entry-meta">
      <span><svg width="9" height="9" viewBox="0 0 10 10" fill="none" stroke="#bc360a" stroke-width="1.2"><circle cx="5" cy="5" r="4"/><path d="M5 2.5 V5 H7"/></svg>March 1, 2015</span>
      <span><svg width="9" height="8" viewBox="0 0 10 8"><path d="M0 1 H4 L5 2 H10 V8 H0 Z" fill="#bc360a"/></svg>Mortgages, Real Estate-Purchases</span>
      <span><svg width="7" height="8" viewBox="0 0 8 9"><circle cx="4" cy="2.2" r="2.2" fill="#bc360a"/><path d="M0 9 Q0 4.5 4 4.5 Q8 4.5 8 9 Z" fill="#bc360a"/></svg>npyrkett</span>
    </div>
    <div class="entry-content">
      <p>Be careful if you are buying a property that the seller is trying to flip. With a flip, the seller buys a distressed or foreclosed property, fixes it up and then quickly resells it. If you are getting an FHA mortgage to buy a&nbsp; property being flipped, you will not be able to <a href="#">sign a contract</a> to purchase the property until 90 days after the seller has owned the property.</p>
      <p>The 90 day time period is measured from the date the seller acquired the property (closed on the property)&nbsp; to the dale the seller signs a contract with the new FHA buyer.<br>
      The purpose of this FHA “<a href="#">seasoning</a>” rule is to prevent sellers from acquiring a property, doing cosmetic repairs and then reselling it at an inflated price. For the past few years, during the depressed real estate market, FHA waived this rule and allowed the buyer to sign the contract earlier than 90 days, but that changed on January 1, 2015.<br>
      But now, FHA is back to enforcing the seasoning requirement.<br>
      I have also found that many lenders will require two appraisals to be done if the buyer is buying a flipped property. This will often delay closing because the parties have to wait for the second appraisal.</p>
    </div>
    <p class="share-heading">Share and Enjoy:</p>
    <div class="share-row"><i></i><i></i><i></i><i></i><i></i><i></i><i></i><i></i><i></i><i></i><i></i><i></i></div>
    <p class="comment-link"><svg width="10" height="9" viewBox="0 0 10 9"><path d="M0 0 H10 V6 H4 L1.5 9 V6 H0 Z" fill="#bc360a"/></svg>Leave a comment</p>
  </article>

  <aside class="widget" style="top:233px;height:101px">
    <h3 class="widget-title">Set an appointment</h3>
    <a href="#">Schedule a phone appointment</a>
    <a href="#">Schedule an office appointment</a>
  </aside>

  <aside class="widget" style="top:352px;height:326px">
    <h3 class="widget-title">Sign up for the Newsletter</h3>
    <p style="margin-bottom:14px">Give us your email and we will send you the newsletter every month</p>
    <label>Email Address*</label><input type="text" aria-label="Email Address">
    <label>First Name</label><input type="text" aria-label="First Name">
    <label>Last Name</label><input type="text" aria-label="Last Name" style="margin-bottom:14px">
    <p>* = required field</p>
    <button class="subscribe">Subscribe</button>
  </aside>

  <aside class="widget" style="top:697px;height:90px">
    <h3 class="widget-title" style="margin-top:0">Categories</h3>
    <a href="#" style="line-height:16px">Bankruptcy <span style="color:#141412">(14)</span></a>
  </aside>
</body>
</html>
```